Stationary Design Foundation Repair Business

We need business card and letterhead design for foundation repair business. Design must compliment the supplied logo. Font is eurostyle. please feel free to ask any questions. Also if we could incorporate the KTW file into the design, but keep the size of it small. Personal details are located in the stationary file.
Updates
I just uploaded a business card design that i like. Just so you guys know what my taste is. Is it possible to create something like this with my business card?
Target Market(s)
Home owners, Builders, Building surveyors, Insurance companies
Industry/Entity Type
Business
Other font styles liked:
- eurostile extended / bold
Look and feel

```html
<!DOCTYPE html>
<html lang="en">
<head>
<meta charset="utf-8">
<title>Firm Base Stationery</title>
<link rel="stylesheet" href="https://fonts.googleapis.com/css2?family=Michroma&family=Arimo:wght@400;700&display=swap">
<style>
:root{
  --backdrop:#dfdfdd;
  --paper:#ffffff;
  --red:#b0221d;
  --ink:#231f20;
  --text:#5a5a5a;
  --muted:#8a8a8a;
  --badge-green:#3c8a3c;
}
*{margin:0;padding:0;box-sizing:border-box}
html,body{width:1200px;height:1041px;overflow:hidden;background:var(--backdrop)}
body{position:relative;font-family:"Arimo",Arial,sans-serif}

.letterhead{position:absolute;left:95px;top:52px;width:660px;height:935px;background:var(--paper)}
.swoosh{position:absolute;left:0;top:0}
.brand{position:absolute;display:flex;align-items:center;gap:8px}
.brand-mark{width:14px;height:14px;background:var(--red)}
.brand-name{font-family:"Michroma",sans-serif;color:var(--ink);letter-spacing:.5px;line-height:1}
.brand-tag{font-family:"Michroma",sans-serif;color:var(--red);letter-spacing:1px;line-height:1;margin-top:4px}
.letterhead .brand{left:340px;top:64px}
.letterhead .brand-name{font-size:19px}
.letterhead .brand-tag{font-size:5.3px}

.letter-body{position:absolute;left:76px;top:188px;width:508px;color:var(--text);font-size:13px;line-height:18.35px}
.salutation{margin-bottom:37px}
.letter-body p.para{text-align:justify;margin-bottom:18.35px}
.sign-name{position:absolute;left:76px;top:666px;font-size:13px;font-weight:700;color:var(--text)}
.signature{position:absolute;left:70px;top:686px;width:150px;height:34px;background:linear-gradient(90deg,#e4eef8,#cfe2f3)}
.sign-role{position:absolute;left:76px;top:721px;font-size:10px;color:var(--muted)}

.foot-bar{position:absolute;top:875px;width:11px;height:35px;background:var(--red)}
.foot-bar.left{left:0}.foot-bar.right{right:0}
.reg-badge{position:absolute;left:38px;top:878px;width:30px;height:30px;border-radius:50%;border:2px solid #9a9a9a}
.reg-plate{position:absolute;left:72px;top:882px;width:70px;height:22px;background:#e6e6e6}
.foot-contact{position:absolute;left:164px;top:872px;font-size:9.6px;line-height:14px;color:var(--ink);font-weight:700}
.member-badge{position:absolute;left:583px;top:870px;width:34px;height:46px;border-radius:4px;background:var(--badge-green)}

.card{position:absolute;left:785px;width:321px;height:182px}
.card-front{top:120px;height:181px;background:var(--ink)}
.card-front .brand{left:33px;top:78px}
.card-front .brand-name{color:#fff;font-size:16px}
.card-front .brand-tag{font-size:4.6px}
.card-back{top:319px;background:var(--paper);overflow:hidden}
.card-back .brand{left:13px;top:24px;gap:6px}
.card-back .brand-mark{width:11px;height:11px}
.card-back .brand-name{font-size:12px}
.card-back .brand-tag{font-size:3.6px;margin-top:3px}
.holder-name{position:absolute;left:13px;top:70px;font-family:"Arimo",sans-serif;font-weight:700;font-size:10px;color:var(--red);letter-spacing:.3px}
.holder-role{position:absolute;left:13px;top:85px;font-size:7.5px;color:var(--ink)}
.card-badge{position:absolute;left:13px;top:112px;width:20px;height:20px;border-radius:50%;border:1.5px solid #9a9a9a}
.card-badge-plate{position:absolute;left:36px;top:114px;width:50px;height:15px;background:#e6e6e6}
.card-contact{position:absolute;right:29px;top:104px;text-align:right;font-size:8.6px;line-height:14.6px;color:var(--ink);font-weight:700}
.card-contact .red{color:var(--red)}
.card-icons{position:absolute;right:15px;top:106px}
.card-swoosh{position:absolute;left:0;bottom:0}
</style>
</head>
<body>

<section class="letterhead">
  <svg class="swoosh" width="660" height="100" viewBox="0 0 660 100">
    <path d="M0,0 H660 C480,6 220,26 0,54 Z" fill="var(--red)"/>
    <path d="M0,62 C150,40 330,22 465,17 C330,30 150,58 0,90 Z" fill="var(--ink)"/>
  </svg>
  <div class="brand">
    <span class="brand-mark"></span>
    <div><div class="brand-name">FIRM BASE</div><div class="brand-tag">PROFESSIONAL UNDERPINNING SERVICES</div></div>
  </div>

  <div class="letter-body">
    <p class="salutation">Dear Sir,</p>
    <p class="para">Lorem Ipsum is simply dummy text of the printing and typesetting industry. Lorem Ipsum has been the industry's standard dummy text ever since the 1500s, when an unknown printer took a galley of type and scrambled it to make a type specimen book. It has survived not only five centuries, but also the leap into electronic typesetting, remaining essentially unchanged. It was popularised in the 1960s with the release of Letraset sheets containing Lorem Ipsum passages, and more recently with desktop publishing software like Aldus PageMaker including versions of Lorem Ipsum.</p>
    <p class="para">Lorem Ipsum is simply dummy text of the printing and typesetting industry. Lorem Ipsum has been the industry's standard dummy text ever since the 1500s, when an unknown printer took a galley of type and scrambled it to make a type specimen book. It has survived not only five centuries, but also the leap into electronic typesetting, remaining essentially unchanged. It was popularised in the 1960s with the release of Letraset sheets containing Lorem Ipsum passages, and more recently with desktop publishing software like Aldus PageMaker including versions of Lorem Ipsum.</p>
    <p class="para">Lorem Ipsum is simply dummy text of the printing and typesetting industry. Lorem Ipsum has been the industry's standard dummy text ever since the 1500s, when an unknown printer took a galley of type and scrambled it to make a type specimen book.</p>
  </div>

  <div class="sign-name">Your Name</div>
  <div class="signature" role="img" aria-label="Handwritten signature"></div>
  <div class="sign-role">CEO &nbsp;|&nbsp; Owner</div>

  <span class="foot-bar left"></span>
  <span class="reg-badge"></span>
  <span class="reg-plate"></span>
  <address class="foot-contact" style="font-style:normal">
    Office &amp; Correspondence: 12 Wattle Crest Way Lindfield Vic 3921<br>
    ABN: 41 205 318 672 &nbsp;|&nbsp; Mobile: 0400 112 908<br>
    Email: info@firmbase.com.au | Website: www.firmbase.com.au
  </address>
  <span class="member-badge"></span>
  <span class="foot-bar right"></span>
</section>

<section class="card card-front">
  <div class="brand">
    <span class="brand-mark"></span>
    <div><div class="brand-name">FIRM BASE</div><div class="brand-tag">PROFESSIONAL UNDERPINNING SERVICES</div></div>
  </div>
</section>

<section class="card card-back">
  <div class="brand">
    <span class="brand-mark"></span>
    <div><div class="brand-name">FIRM BASE</div><div class="brand-tag">PROFESSIONAL UNDERPINNING SERVICES</div></div>
  </div>
  <div class="holder-name">MARCUS HALLETT</div>
  <div class="holder-role">Proprietor</div>
  <span class="card-badge"></span>
  <span class="card-badge-plate"></span>
  <address class="card-contact" style="font-style:normal">
    12 Wattle Crest Way Lindfield Vic 3921<br>
    <span class="red">ABN:</span> 41 205 318 672 &nbsp;|&nbsp; 0400 112 908<br>
    info@firmbase.com.au<br>
    www.firmbase.com.au
  </address>
  <svg class="card-icons" width="9" height="56" viewBox="0 0 9 56" fill="var(--red)">
    <path d="M4.5,0 A3.2,3.2 0 0 1 7.7,3.2 C7.7,5.5 4.5,8.5 4.5,8.5 C4.5,8.5 1.3,5.5 1.3,3.2 A3.2,3.2 0 0 1 4.5,0 Z M4.5,2 A1.2,1.2 0 1 0 4.5,4.4 A1.2,1.2 0 1 0 4.5,2 Z"/>
    <path d="M0.5,19 C2,16 7,16 8.5,19 L7,20.5 L5.8,19 H3.2 L2,20.5 Z M2,20.5 H7 V22.5 H2 Z"/>
    <rect x="0.5" y="31" width="8" height="5.5"/>
    <path d="M0.5,31 L4.5,34 L8.5,31" stroke="#fff" stroke-width="0.8" fill="none"/>
    <circle cx="4.5" cy="48" r="3.7"/>
    <path d="M0.8,48 H8.2 M4.5,44.3 V51.7 M4.5,44.3 C2.5,46 2.5,50 4.5,51.7 C6.5,50 6.5,46 4.5,44.3" stroke="#fff" stroke-width="0.5" fill="none"/>
  </svg>
  <svg class="card-swoosh" width="321" height="50" viewBox="0 0 321 50">
    <path d="M0,22 C100,26 200,36 321,50 H0 Z" fill="var(--red)"/>
    <path d="M0,4 C90,14 160,28 215,44 C150,32 80,22 0,18 Z" fill="var(--ink)"/>
  </svg>
</section>

</body>
</html>
```